Dancing Beyond Dawn Book Cover

We are looking for a book cover that will capture the audience who are GEN X and Boomer Women looking to change their life. We need the book cover to be in alignment with our Brand DancingBeyondDawn.example

Target Market(s)

women 45+

Font styles to use
Other font styles liked:
• Montserrat

Colors
EE7325
F08F49
F5BC92
FAE3D3
FDF4ED
EB3D1F
EC4F4E
F09395
F8D3D4
FCEDEE
E54698
E96AAD
F1A4CE
F9D9EA
FCEFF6

Requirements
Must have
• FUN
Should not have
• too cutsey!

```html
<!DOCTYPE html>
<html lang="en">
<head>
<meta charset="utf-8">
<title>Dancing Beyond Dawn — Book Cover</title>
<link rel="stylesheet" href="https://fonts.googleapis.com/css2?family=Montserrat:wght@300;400;800;900&display=swap">
<style>
  :root {
    --backdrop: #fdf0f0;
    --cover-white: #ffffff;
    --coral: #f28a86;
    --blush: #f8d3d4;
    --blush-light: #fcedee;
  }
  * { margin: 0; padding: 0; box-sizing: border-box; }
  html, body {
    width: 1200px;
    height: 1200px;
    overflow: hidden;
    background: var(--backdrop);
  }
  .stage {
    position: relative;
    width: 1200px;
    height: 1200px;
  }
  .book-cover {
    position: absolute;
    left: 264px;
    top: 114px;
    width: 674px;
    height: 972px;
    background: var(--cover-white);
    border-radius: 10px;
    overflow: hidden;
    font-family: "Montserrat", sans-serif;
    box-shadow: 18px 22px 40px rgba(200, 140, 140, 0.25);
  }
  .title-panel {
    position: absolute;
    inset: 0;
    width: 674px;
    height: 972px;
  }
  .illustration-area {
    position: absolute;
    left: 146px;
    top: 470px;
    width: 382px;
    height: 476px;
    border-radius: 28px;
    background: linear-gradient(180deg, var(--coral) 0%, var(--blush) 55%, var(--blush-light) 100%);
  }
  .title {
    position: absolute;
    left: 0;
    right: 0;
    top: 48px;
    text-align: center;
    color: var(--cover-white);
  }
  .title-light {
    display: block;
    font-weight: 300;
    font-size: 92px;
    line-height: 92px;
    letter-spacing: 3px;
  }
  .title-bold {
    display: block;
    margin-top: 6px;
    font-weight: 900;
    font-size: 104px;
    line-height: 100px;
    letter-spacing: 2px;
  }
  .title-band {
    position: absolute;
    left: 58px;
    top: 236px;
    width: 558px;
    height: 98px;
    background: var(--cover-white);
    display: flex;
    align-items: center;
    justify-content: center;
  }
  .title-band span {
    color: var(--coral);
    font-weight: 900;
    font-size: 80px;
    letter-spacing: 3px;
    line-height: 1;
  }
  .subtitle {
    position: absolute;
    left: 0;
    right: 0;
    top: 366px;
    text-align: center;
    color: var(--cover-white);
    font-weight: 400;
    font-size: 27px;
    line-height: 34px;
  }
</style>
</head>
<body>
  <main class="stage">
    <article class="book-cover">
      <svg class="title-panel" viewBox="0 0 674 972" aria-hidden="true">
        <path fill="var(--coral)"
          d="M0 0 H674 V470 C650 500 600 500 580 545 C560 590 520 640 440 660
             H234 C154 640 114 590 94 545 C74 500 24 500 0 470 Z"/>
      </svg>

      <div class="illustration-area" role="img"
        aria-label="Illustration of a woman with long flowing hair, eyes closed, hugging a large heart"></div>

      <h1 class="title">
        <span class="title-light">DANCING</span>
        <span class="title-bold">BEYOND</span>
      </h1>
      <div class="title-band"><span>DAWN</span></div>

      <p class="subtitle">A woman's guide to living it up<br>without the booze</p>
    </article>
  </main>
</body>
</html>
```